Packaging for a Herbal Coffee Brand

We need packaging for a herbal coffee brand. I want the packaging to be fun, bright and have some image of coffee drink (NO BEANS as it does not contain coffee) on it.

The product is called Coffee Substitute. It's gluten-free, acid-free and caffeine free

Ingredients
organic roasted chicory powder, organic roasted carob powder, and organic roasted dandelion root powder

Preparation Instructions - Coffee Press or Tea Straner

1. For each 6 oz of water add 1-2 heaping teaspoons of Zest coffee substitute to a coffee press or tea strainer (add more or less water depending on your strength preference)
2. Pour hot water—not quite boiling—into the pot/cup, and gently stir
3. Let stand for 10-15 seconds then press the plunger down slowly, or remove the strainer.
4. Zest and enjoy! (see what we did there?)

"Use By" line: Best if used within 6 months of opening

Statements regarding dietary supplements have not been evaluated by the BHQ and are not intended to diagnose, treat, cure, or prevent any disease or health condition.

Target Market(s)

Health oriented women who can not drink coffee but want to enjoy the flavor of it.

Font styles to use
Sans Serif

Requirements
Must have
• An image of coffee. I'm cool if this is graphics or literally a cup of coffee on it.

some inspiration:
https://weareloma.example/collections/bestsellers/products/original-loma
https://vornikfoods.example/products/new-product-quikmix

Please make sure to follow these rules when designing per our printer - https://trundowrap.example/wp-content/uploads/2020/02/Prepress-Checklist-Rev9.pdf Standard Stand up pouch - that is Height x Width x Gusset: 9 x 6 x 3-1/2 inches 230 x 150 x 90 mm Location of Zipper (Bottom-of-Bag to Bottom-of-Zipper): 7-5/8 inches or 192 mm See this also https://trundowrap.example/wp-content/uploads/2020/02/LR-Submitting-Artwork-Guidelines-Side-to-Side-Registration.pdf
Nice to have
• Really FUN, BOLD,
Should not have
• Boring, plain, NO coffee beans. Should be CLEAR that it is a coffee substitute

```html
<!DOCTYPE html>
<html lang="en">
<head>
<meta charset="utf-8">
<title>Zest Herbals – Coffee Substitute Pouch Front</title>
<link rel="stylesheet" href="https://fonts.googleapis.com/css2?family=Great+Vibes&family=Rye&family=Oswald:wght@600&family=Roboto+Condensed:wght@400&display=swap">
<style>
  :root {
    --stage: #2a2a2a;
    --paper: #f8f8f8;
    --paper-edge: #efefef;
    --sun: #ecc21f;
    --sun-soft: #f3d25a;
    --ink: #1e1e1e;
    --leaf: #3f9a2c;
    --leaf-dark: #2b7a1d;
    --cup-rim: #f4f2ee;
    --crema: #b98a4e;
    --crema-dark: #8a5a24;
    --handle: #d81f1f;
  }
  * { margin: 0; padding: 0; box-sizing: border-box; }
  html, body {
    width: 1200px; height: 913px; overflow: hidden;
    background: var(--stage);
  }
  .canvas {
    position: relative; width: 1200px; height: 913px;
  }
  .pouch-front {
    position: absolute; left: 319px; top: 26px;
    width: 561px; height: 860px;
    background: radial-gradient(ellipse at 50% 40%, var(--paper) 60%, var(--paper-edge) 100%);
  }
  .pouch-front svg { display: block; width: 100%; height: 100%; }
  .brand-name { font-family: "Roboto Condensed", sans-serif; font-weight: 400; fill: var(--ink); }
  .flavour { font-family: "Great Vibes", cursive; fill: var(--ink); }
  .headline-coffee { font-family: "Rye", serif; fill: var(--sun); }
  .headline-substitute { font-family: "Oswald", sans-serif; font-weight: 600; fill: var(--ink); }
  .tagline { font-family: "Roboto Condensed", sans-serif; fill: var(--ink); letter-spacing: 0.5px; }
  .badge-ring { fill: none; stroke: var(--ink); stroke-width: 2.2; }
  .badge-slash { stroke: var(--ink); stroke-width: 2; }
  .badge-label { font-family: "Roboto Condensed", sans-serif; font-size: 4.2px; font-weight: 400; fill: var(--ink); }
</style>
</head>
<body>
<main class="canvas">
  <section class="pouch-front">
    <svg viewBox="0 0 561 860" xmlns="http://www.w3.org/2000/svg">
      <defs>
        <radialGradient id="ornament-tone" cx="50%" cy="0%" r="100%">
          <stop offset="0%" stop-color="#f6dc78" stop-opacity="0.55"/>
          <stop offset="100%" stop-color="#f6dc78" stop-opacity="0.12"/>
        </radialGradient>
        <radialGradient id="coffee-tone" cx="45%" cy="45%" r="60%">
          <stop offset="0%" stop-color="var(--crema)"/>
          <stop offset="100%" stop-color="var(--crema-dark)"/>
        </radialGradient>
      </defs>

      <path class="mandala-ornament" role="img" aria-label="Golden mandala ornament fanning down from the top edge"
            d="M101 0 A180 202 0 0 0 461 0 Z" fill="url(#ornament-tone)"/>

      <g class="brand-lockup">
        <text class="brand-name" x="283" y="185" text-anchor="middle" font-size="40">Zest</text>
        <text class="brand-name" x="283" y="228" text-anchor="middle" font-size="30">Herbals</text>
      </g>

      <g class="coffee-cup" role="img" aria-label="Top-down photo of a white cup of frothy herbal coffee with a red handle">
        <ellipse cx="295" cy="392" rx="134" ry="132" fill="#d9d9d9" opacity="0.45"/>
        <rect x="390" y="390" width="58" height="32" rx="14" fill="var(--handle)"/>
        <circle cx="283" cy="379" r="130" fill="var(--cup-rim)"/>
        <circle cx="283" cy="379" r="106" fill="url(#coffee-tone)"/>
      </g>

      <g class="leaves" role="img" aria-label="Scattered fresh green leaves">
        <ellipse cx="130" cy="74" rx="40" ry="14" transform="rotate(-4 130 74)" fill="var(--leaf)"/>
        <ellipse cx="525" cy="80" rx="34" ry="14" transform="rotate(-12 525 80)" fill="var(--leaf)"/>
        <ellipse cx="395" cy="196" rx="44" ry="14" transform="rotate(4 395 196)" fill="var(--leaf)"/>
        <ellipse cx="33" cy="218" rx="34" ry="15" transform="rotate(-8 33 218)" fill="var(--leaf)"/>
        <ellipse cx="520" cy="305" rx="40" ry="15" transform="rotate(10 520 305)" fill="var(--leaf)"/>
        <ellipse cx="38" cy="470" rx="40" ry="12" transform="rotate(6 38 470)" fill="var(--leaf-dark)"/>
        <ellipse cx="535" cy="535" rx="28" ry="12" transform="rotate(-20 535 535)" fill="var(--leaf)"/>
        <ellipse cx="508" cy="770" rx="24" ry="9" transform="rotate(-16 508 770)" fill="var(--leaf)"/>
        <ellipse cx="40" cy="810" rx="44" ry="12" transform="rotate(-12 40 810)" fill="var(--leaf-dark)"/>
      </g>

      <text class="flavour" x="283" y="545" text-anchor="middle" font-size="70">Original</text>

      <text class="headline-coffee" x="81" y="663" font-size="128"
            textLength="393" lengthAdjust="spacingAndGlyphs">COFFEE</text>

      <text class="headline-substitute" x="83" y="748" font-size="94"
            textLength="390" lengthAdjust="spacingAndGlyphs">SUBSTITUTE</text>

      <text class="tagline" x="283" y="774" text-anchor="middle" font-size="14.5">ADAPTOGENIC COFFEE ALTERNATIVE</text>

      <g class="claim-badges">
        <g class="badge" transform="translate(228 806)">
          <circle class="badge-ring" r="20"/>
          <line class="badge-slash" x1="-12" y1="12" x2="12" y2="-12"/>
          <text class="badge-label" y="11" text-anchor="middle">GLUTEN</text>
          <text class="badge-label" y="15.5" text-anchor="middle">FREE</text>
        </g>
        <g class="badge" transform="translate(279 806)">
          <circle class="badge-ring" r="20"/>
          <line class="badge-slash" x1="-12" y1="12" x2="12" y2="-12"/>
          <text class="badge-label" y="11" text-anchor="middle">ACID</text>
          <text class="badge-label" y="15.5" text-anchor="middle">FREE</text>
        </g>
        <g class="badge" transform="translate(331 806)">
          <circle class="badge-ring" r="20"/>
          <line class="badge-slash" x1="-12" y1="12" x2="12" y2="-12"/>
          <text class="badge-label" y="11" text-anchor="middle">CAFFEINE</text>
          <text class="badge-label" y="15.5" text-anchor="middle">FREE</text>
        </g>
      </g>
    </svg>
  </section>
</main>
</body>
</html>
```